Surgical Procedure Room Letterhead

PLEASE DO NOT MAKE YOUR LETTERHEAD SIMILAR TO THE ONE I AM INCLUDING IN MY UPLOADS

Hello! I need my logo used to make a very clean, professional, simple letterhead that has all the pertinent information in it:
Location: 4829 NW 58th Lane, Suite 310
Cedar Bluff, GA 33468
Phone: 561-618-2450
Fax: 800-394-8261

Can you please put this all on a word document that is easily editable? I will include my practice letterhead as an example ONLY of how easy it should be to write below the letterhead. Please don't make this letterhead the same as the one I am including in this example. They are two separate businesses.

Target Market(s)

Insurance companies

Industry/Entity Type

medical

Requirements
Must have
• classiness, elegance, simplicity
Should not have
• Please don't make your letterhead the same as the one that I included in my uploads

```html
<!DOCTYPE html>
<html lang="en">
<head>
<meta charset="utf-8">
<title>Medvale Suites Letterhead</title>
<link rel="stylesheet" href="https://fonts.googleapis.com/css2?family=Cinzel:wght@400;500&family=Roboto+Slab:wght@700&family=Satisfy&display=block">
<style>
  :root {
    --navy: #00305b;
    --gold: #d9b33c;
    --ink: #1e1e1e;
    --paper: #ffffff;
  }
  * { margin: 0; padding: 0; box-sizing: border-box; }
  html, body { width: 767px; height: 1200px; overflow: hidden; background: var(--paper); }
  .letterhead { position: relative; width: 767px; height: 1200px; background: var(--paper); overflow: hidden; }
  .bands { position: absolute; left: 0; top: 0; width: 767px; height: 1200px; }
  .brand {
    position: absolute; left: 46px; top: 58px;
    display: flex; align-items: center; gap: 10px;
    font-family: "Cinzel", serif; font-weight: 500; font-size: 19px;
    color: var(--navy); letter-spacing: 0.5px;
  }
  .brand-mark { width: 26px; height: 26px; border-radius: 50%; background: var(--gold); }
  .recipient {
    position: absolute; left: 96px; top: 340px;
    font-family: "Roboto Slab", Georgia, serif; font-weight: 700; font-size: 20px; color: var(--ink);
  }
  .body-copy {
    position: absolute; left: 86px; width: 602px;
    font-family: "Cinzel", serif; font-size: 12px; line-height: 18.8px; color: var(--ink);
  }
  .p1 { top: 402px; }
  .p2 { top: 580px; }
  .p3 { top: 654px; }
  .signature {
    position: absolute; left: 518px; top: 818px;
    font-family: "Satisfy", "Brush Script MT", cursive; font-size: 29px; color: var(--ink);
  }
  .contact {
    position: absolute; left: 40px;
    display: flex; align-items: center;
    font-family: "Cinzel", serif; font-size: 16px; color: var(--navy);
  }
  .contact svg { width: 10px; height: 12px; margin-right: 17px; }
  .contact-phones { top: 1114px; }
  .contact-address { top: 1140px; }
  .contact-phones .gap { width: 36px; }
</style>
</head>
<body>
<div class="letterhead">
  <svg class="bands" viewBox="0 0 767 1200" aria-hidden="true">
    <polygon points="273,0 767,0 767,39 312,39" fill="var(--navy)"/>
    <polygon points="320,52 767,52 767,80 355,80" fill="var(--gold)"/>
    <polygon points="0,1169 447,1169 416,1200 0,1200" fill="var(--gold)"/>
    <polygon points="458,1169 767,1169 767,1200 428,1200" fill="var(--navy)"/>
  </svg>

  <div class="brand"><span class="brand-mark"></span><span class="brand-name">Medvale Suites</span></div>

  <div class="recipient">Daniel Hart</div>

  <p class="body-copy p1">Lorem Ipsum is simply dummy text of the printing and typesetting industry. Lorem Ipsum has been the industry's standard dummy text ever since the 1500s, when an unknown printer took a galley of type and scrambled it to make a type specimen book. It has survived not only five centuries, but also the leap into electronic typesetting, remaining essentially unchanged. It was popularised in the 1960s with the release of Presstype sheets containing Lorem Ipsum passages, and more recently with desktop publishing software like Folio Composer including versions of Lorem Ipsum.</p>

  <p class="body-copy p2">Contrary to popular belief, Lorem Ipsum is not simply random text. It has roots in a piece of classical Latin literature from 45 BC, making it over 2000 years old.</p>

  <p class="body-copy p3">Thomas Whitford, a Latin professor at Ashbury College in Virginia, looked up one of the more obscure Latin words, consectetur, from a Lorem Ipsum passage, and going through the cites of the word in classical literature, discovered the undoubtable source. Lorem Ipsum comes from sections</p>

  <div class="signature">Daniel Hart</div>

  <div class="contact contact-phones">
    <svg viewBox="0 0 10 12" aria-hidden="true"><rect x="2" y="0.5" width="6" height="11" rx="1.2" fill="none" stroke="var(--navy)" stroke-width="1.2"/><circle cx="5" cy="9.3" r="0.7" fill="var(--navy)"/></svg>
    <span>561-618-2450</span>
    <span class="gap"></span>
    <svg viewBox="0 0 10 12" aria-hidden="true"><rect x="1" y="3" width="8" height="6" rx="1" fill="none" stroke="var(--navy)" stroke-width="1.1"/><rect x="3" y="1" width="4" height="3" fill="none" stroke="var(--navy)" stroke-width="1"/></svg>
    <span>800-394-8261</span>
  </div>

  <div class="contact contact-address">
    <svg viewBox="0 0 10 12" aria-hidden="true"><path d="M5 11.5 C2 7.5 1 6 1 4.5 A4 4 0 0 1 9 4.5 C9 6 8 7.5 5 11.5 Z" fill="var(--navy)"/><circle cx="5" cy="4.5" r="1.5" fill="#fff"/></svg>
    <span>4829 NW 58th Lane, Suite 310 Cedar Bluff, GA 33468</span>
  </div>
</div>
</body>
</html>
```